Blog based website for baseball.

I am a college baseball coach looking to create a blog type site that uses content to keep readers coming back and eventually trusting me enough to buy my products.

I am an author, coach, writer, speaker with a bunch sites now, but I want to make one main site that people can come back to and see new content over and over..

Target Market(s)

High school baseball players and parents.

Industry/Entity Type

Education

Number of Pages Required

4 page

Font styles to use
Sans Serif

Requirements
Must have
• 1) An about page. 2) Either commerce page or link to my other commerce pages. 3) Featured blog but also access to past blogs. 4) Featured product of the week (maybe in side bar). 5) Places to opt in and join the list. 6) A way to share the content people like.
Nice to have
• No idea the difference between uncoded and coded!
• I like the idea of an opt in pop up.

```html
<!DOCTYPE html>
<html lang="en">
<head>
<meta charset="utf-8">
<title>Dale Whitcomb Baseball Blog</title>
<link href="https://fonts.googleapis.com/css2?family=Open+Sans:wght@400;600;800&display=swap" rel="stylesheet">
<style>
  :root {
    --navy: #1b3682;
    --navy-deep: #142a6b;
    --blue-text: #1f3f9a;
    --panel: #dcdcdc;
    --white: #ffffff;
    --ink: #333333;
    --muted: #666666;
    --rule: #d0d0d0;
    --footnote: #a9b8e6;
  }
  * { box-sizing: border-box; margin: 0; padding: 0; }
  html, body { width: 1200px; height: 2528px; overflow: hidden; background: var(--white); }
  body { position: relative; font-family: "Open Sans", Verdana, sans-serif; color: var(--ink); }

  .site-header { position: absolute; left: 0; top: 0; width: 1200px; height: 220px; background: var(--white); }
  .coach-photo { position: absolute; left: 48px; top: 0; width: 152px; height: 112px;
    background: linear-gradient(180deg, #c9ced8 0%, #4a5a7a 55%, #1b2540 100%); }
  .site-title { position: absolute; left: 48px; top: 126px; width: 1104px; text-align: center;
    font-size: 56px; font-weight: 800; color: var(--blue-text); white-space: nowrap; line-height: 1; }
  .login { position: absolute; left: 1000px; top: 30px; font-size: 18px; color: var(--ink); }
  .social { position: absolute; top: 26px; width: 30px; height: 30px; border-radius: 50%; background: var(--navy); }

  .main-nav { position: absolute; left: 0; top: 220px; width: 1200px; height: 68px; background: var(--navy);
    display: flex; justify-content: center; align-items: center; gap: 90px; }
  .main-nav a, .footer-nav a { color: var(--white); text-decoration: none; font-size: 17px; font-weight: 600; }

  .page-panel { position: absolute; left: 48px; top: 304px; width: 1112px; height: 1996px; background: var(--panel); }
  .blog-column { position: absolute; left: 80px; top: 320px; width: 792px; height: 1900px; background: var(--white); }

  .date-bar { position: absolute; left: 112px; width: 728px; height: 52px; background: var(--navy);
    color: var(--white); font-size: 17px; font-weight: 600; padding: 14px 20px; }
  .excerpt { position: absolute; left: 112px; width: 728px; font-size: 16px; color: var(--blue-text);
    white-space: nowrap; overflow: hidden; }
  .post-image { position: absolute; left: 112px; width: 728px; }
  .play-button { position: absolute; width: 64px; height: 64px; border-radius: 50%; background: var(--white); }
  .play-button svg { position: absolute; left: 24px; top: 18px; }

  .sidebar-bar { position: absolute; left: 896px; width: 232px; height: 56px; background: var(--navy);
    color: var(--white); font-size: 17px; font-weight: 600; text-align: center; padding-top: 15px; }
  .popular-list { position: absolute; left: 896px; top: 380px; width: 232px; height: 380px; background: var(--white);
    list-style: none; padding: 10px 14px; }
  .popular-list li { height: 60px; border-bottom: 2px solid var(--rule); padding-top: 6px; font-size: 15px; color: var(--ink); }
  .popular-list li span { display: block; font-size: 11px; color: var(--muted); }

  .product-list { position: absolute; left: 896px; top: 840px; width: 232px; height: 1380px; background: var(--white); }
  .product { position: absolute; left: 14px; width: 204px; border-bottom: 2px solid var(--rule); }
  .product p { font-size: 11px; line-height: 15px; color: var(--ink); }
  .product-image { margin: 10px auto 0; }
  .read-more { display: block; text-align: center; font-size: 14px; color: var(--blue-text); padding: 8px 0 10px; }

  .site-footer { position: absolute; left: 0; top: 2352px; width: 1200px; height: 176px; background: var(--navy); }
  .footer-nav { position: absolute; top: 28px; width: 1200px; display: flex; justify-content: center; gap: 90px; }
  .footer-rule { position: absolute; left: 0; top: 78px; width: 1200px; height: 3px; background: var(--white); }
  .copyright { position: absolute; top: 128px; width: 1200px; text-align: center; font-size: 14px; color: var(--footnote); }
</style>
</head>
<body>
  <header class="site-header">
    <div class="coach-photo" role="img" aria-label="Portrait of the coach in a dark suit"></div>
    <h1 class="site-title">DALE WHITCOMB BASEBALL BLOG</h1>
    <span class="login">Login</span>
    <span class="social" style="left:1076px" aria-label="Share"></span>
    <span class="social" style="left:1124px" aria-label="Share"></span>
  </header>

  <nav class="main-nav"><a href="#">BLOG</a><a href="#">ABOUT ME</a><a href="#">SHOP</a></nav>

  <div class="page-panel"></div>
  <main class="blog-column"></main>

  <article>
    <div class="date-bar" style="top:328px">June 15, 2015</div>
    <p class="excerpt" style="top:394px">Lorem ipsum dolor sit amet, consectetur adipiscing elit, sed do eiusmod tempor incididunt...</p>
    <div class="post-image" style="top:432px;height:520px;background:linear-gradient(180deg,#3a63b8 0%,#2d55a8 50%,#6a8a4a 80%,#b07a55 100%)" role="img" aria-label="Batter in a white uniform swinging at home plate with the catcher behind"></div>
    <div class="play-button" style="left:472px;top:660px"><svg width="22" height="28"><polygon points="0,0 22,14 0,28" fill="#1b3682"/></svg></div>
  </article>

  <article>
    <div class="date-bar" style="top:992px">June 14, 2015</div>
    <p class="excerpt" style="top:1058px">Lorem ipsum dolor sit amet, consectetur adipiscing elit, sed do eiusmod tempor incididunt...</p>
    <div class="post-image" style="top:1100px;height:412px;background:linear-gradient(180deg,#1e2a3a 0%,#4a5a4a 40%,#5f8a48 70%,#b07a55 100%)" role="img" aria-label="Batter sliding past the catcher and umpire at home plate"></div>
    <div class="play-button" style="left:472px;top:1260px"><svg width="22" height="28"><polygon points="0,0 22,14 0,28" fill="#1b3682"/></svg></div>
  </article>

  <article>
    <div class="date-bar" style="top:1560px">June 13, 2015</div>
    <p class="excerpt" style="top:1626px">Lorem ipsum dolor sit amet, consectetur adipiscing elit, sed do eiusmod tempor incididunt...</p>
    <div class="post-image" style="top:1668px;height:480px;background:linear-gradient(180deg,#2a2e36 0%,#5a6c8c 40%,#d8dce6 70%,#8a8f9a 100%)" role="img" aria-label="Teammates in pinstripe uniforms celebrating together"></div>
  </article>

  <aside>
    <div class="sidebar-bar" style="top:324px">Most popular</div>
    <ul class="popular-list">
      <li>June 15, 2015<span>Lorem ipsum dolor sit amet</span></li>
      <li>June 15, 2015<span>Lorem ipsum dolor sit amet</span></li>
      <li>June 15, 2015<span>Lorem ipsum dolor sit amet</span></li>
      <li>June 15, 2015<span>Lorem ipsum dolor sit amet</span></li>
      <li>June 15, 2015<span>Lorem ipsum dolor sit amet</span></li>
      <li>June 15, 2015<span>Lorem ipsum dolor sit amet</span></li>
    </ul>

    <div class="sidebar-bar" style="top:784px">New Products</div>
    <div class="product-list">
      <div class="product" style="top:20px">
        <p>Lorem ipsum dolor sit amet consectetur elit sed</p>
        <div class="product-image" style="width:180px;height:220px;background:linear-gradient(160deg,#c8302a,#e8e4dc 60%,#1b3682)" role="img" aria-label="Book cover about playing college baseball"></div>
        <a class="read-more" href="#">Read more</a>
      </div>
      <div class="product" style="top:360px">
        <p>Lorem ipsum dolor sit amet consectetur elit sed</p>
        <div class="product-image" style="width:130px;height:196px;background:linear-gradient(180deg,#d8d4cc,#8a1e1e 60%,#3a2a2a)" role="img" aria-label="Red book cover with a baseball player"></div>
        <a class="read-more" href="#">Read more</a>
      </div>
      <div class="product" style="top:690px">
        <p>Lorem ipsum dolor sit amet consectetur elit sed</p>
        <div class="product-image" style="width:150px;height:212px;background:linear-gradient(180deg,#1a2440 0%,#f2f2f2 35%,#e6e6e6 100%)" role="img" aria-label="White baseball jersey with number 24"></div>
        <a class="read-more" href="#">Read more</a>
      </div>
      <div class="product" style="top:1030px;border-bottom:none">
        <p>Lorem ipsum dolor sit amet consectetur elit sed</p>
        <div class="product-image" style="width:150px;height:170px;margin-top:40px;border-radius:50%;background:radial-gradient(circle at 40% 40%,#ffffff,#dcdcdc 70%,#b8b8b8)" role="img" aria-label="Baseball"></div>
        <a class="read-more" href="#">Read more</a>
      </div>
    </div>
  </aside>

  <footer class="site-footer">
    <nav class="footer-nav"><a href="#">BLOG</a><a href="#">ABOUT ME</a><a href="#">SHOP</a></nav>
    <div class="footer-rule"></div>
    <p class="copyright">copyright Whitcomb 2015</p>
  </footer>
</body>
</html>
```